Business Card & Logo Design - Hedge Fund

We need a business card and logo design for a hedge fund. The hedge fund is named Morvane Equity LLC. Morvane Equity was created by finance professors and the strategy is based academic research that looks for patterns in stock prices. The design should look conservative, solid, strong. We favor a classic style - nothing flashy. The logo can relate to the name Morvane Equity, or it could involve a symbol design that connotes "science" . We are open to ideas. We do not want alot of colors - but if any, color - blue is preferred. The font that seems to look best for the name (Morvane Equity) is arial black. We are open to ideas. Most important - we want to see a mock up of an actual business card with the logo concept embedded. The business card should include space for : company name, individual name, position title, cell phone, address. We hope to have this work done by Sept. 8.

Target Market(s)

We will be meeting with and giving the business card to institutions and high net worth individuals.

Industry/Entity Type

Investment Advisory

Contact Information for Business Card

Company name - Morvane Equity LLC
Individual name - Peter Dalby
Title - Portfolio Manager
Cell - (412) 555-0187
Address - 2650 Birchmont Lane, Suite 300, Atlanta GA 30327

Font styles to use
Other font styles liked:
• Arial

Colors
3277b5
0255a3
85acd3
cedeed
fdf9cf
d9d9d9
e6e6e6
f04a50
6b449b

Requirements
Must have
• Must have card details that are sited above.
• We would like a logo related to the name (Morvane Equity) or concept of the fund.
Nice to have
• We want conservative / understated / clean crisp look.
• If any colors - we prefer conservative appearance - blue / gray.
• I have enclosed an example of a card style that looks attractive - please do not exactly copy this card. This is not our company or logo. I feel the layout is attractive - just as an example
Should not have
• Avoid too much color.
• I have selected some preferred colors. Please do not use all of the colors - I have selected a few that might work - but I am not sure. We are open to your ideas so please do not feel the need to use all or any of these.

```html
<!DOCTYPE html>
<html lang="en">
<head>
<meta charset="utf-8">
<title>Morvane Equity LLC – Business Card</title>
<link href="https://fonts.googleapis.com/css2?family=Lato:wght@400;700;900&display=swap" rel="stylesheet">
<style>
  :root {
    --page-bg: #e9e9e9;
    --card-white: #ffffff;
    --ink: #2b2b2b;
    --ink-soft: #3d3d3d;
    --brand-blue: #2f86c9;
    --blue-light: #3a97d6;
    --blue-deep: #0f5fa6;
    --on-blue: #ffffff;
  }
  * { margin: 0; padding: 0; box-sizing: border-box; }
  html, body { width: 1200px; height: 942px; overflow: hidden; }
  body {
    background: var(--page-bg);
    font-family: "Lato", Arial, sans-serif;
    display: flex;
    align-items: center;
    justify-content: center;
    gap: 40px;
  }
  .card {
    width: 540px;
    height: 309px;
    border-radius: 3px;
    box-shadow: 0 6px 18px rgba(0,0,0,0.18);
    position: relative;
    overflow: hidden;
  }

  /* Front */
  .card-front {
    background: linear-gradient(135deg, #f3f3f3 0%, var(--card-white) 55%, #f6f6f6 100%);
    display: flex;
    align-items: center;
  }
  .front-brand {
    width: 250px;
    display: flex;
    align-items: center;
    justify-content: center;
    gap: 10px;
  }
  .brand-mark {
    width: 14px; height: 14px;
    background: var(--brand-blue);
  }
  .brand-name {
    font-weight: 900;
    color: var(--ink);
    font-size: 22px;
    line-height: 1.05;
    letter-spacing: 0.5px;
    text-transform: uppercase;
  }
  .divider {
    width: 2px;
    height: 170px;
    background: var(--brand-blue);
  }
  .front-details {
    padding-left: 30px;
    color: var(--ink-soft);
  }
  .person-name {
    font-weight: 900;
    font-size: 20px;
    color: var(--ink);
    letter-spacing: 0.3px;
    text-transform: uppercase;
  }
  .person-title {
    font-size: 14px;
    color: var(--brand-blue);
    letter-spacing: 0.6px;
    text-transform: uppercase;
    margin-bottom: 16px;
  }
  .contact-line {
    display: flex;
    align-items: flex-start;
    gap: 9px;
    font-size: 14px;
    line-height: 1.45;
    margin-bottom: 4px;
  }
  .contact-line svg {
    width: 12px; height: 12px;
    margin-top: 4px;
    flex: none;
    fill: var(--brand-blue);
  }

  /* Back */
  .card-back {
    background: linear-gradient(160deg, var(--blue-light) 0%, var(--brand-blue) 45%, var(--blue-deep) 100%);
    display: flex;
    flex-direction: column;
    align-items: center;
    justify-content: center;
    color: var(--on-blue);
    text-align: center;
  }
  .back-brand {
    display: flex;
    align-items: center;
    gap: 12px;
  }
  .back-brand .brand-mark { background: var(--on-blue); width: 16px; height: 16px; }
  .back-brand .brand-name { color: var(--on-blue); font-size: 30px; }
  .website {
    margin-top: 22px;
    font-size: 13px;
    letter-spacing: 2.5px;
    text-transform: uppercase;
  }
</style>
</head>
<body>
  <section class="card card-front">
    <div class="front-brand">
      <span class="brand-mark"></span>
      <div class="brand-name">Morvane<br>Equity LLC</div>
    </div>
    <div class="divider"></div>
    <div class="front-details">
      <div class="person-name">Peter Dalby</div>
      <div class="person-title">Portfolio Manager</div>
      <div class="contact-line">
        <svg viewBox="0 0 24 24" aria-hidden="true"><path d="M6.6 10.8a15.1 15.1 0 0 0 6.6 6.6l2.2-2.2c.3-.3.7-.4 1-.2 1.1.4 2.3.6 3.6.6.6 0 1 .4 1 1V20c0 .6-.4 1-1 1A17 17 0 0 1 3 4c0-.6.4-1 1-1h3.5c.6 0 1 .4 1 1 0 1.3.2 2.5.6 3.6.1.3 0 .7-.2 1z"/></svg>
        <span>(412) 555-0187</span>
      </div>
      <div class="contact-line">
        <svg viewBox="0 0 24 24" aria-hidden="true"><path d="M2 5h20v14H2z M2 5l10 8 10-8" fill="none" stroke="#2f86c9" stroke-width="2.4"/></svg>
        <span>pdalby@morvaneequity.com</span>
      </div>
      <div class="contact-line">
        <svg viewBox="0 0 24 24" aria-hidden="true"><path d="M12 2a7 7 0 0 0-7 7c0 5.2 7 13 7 13s7-7.8 7-13a7 7 0 0 0-7-7zm0 9.5a2.5 2.5 0 1 1 0-5 2.5 2.5 0 0 1 0 5z"/></svg>
        <span>2650 Birchmont Lane,<br>Suite 300, Atlanta GA 30327</span>
      </div>
    </div>
  </section>

  <section class="card card-back">
    <div class="back-brand">
      <span class="brand-mark"></span>
      <div class="brand-name">Morvane<br>Equity LLC</div>
    </div>
    <div class="website">www.morvaneequity.com</div>
  </section>
</body>
</html>
```